Brightpath Holdings Business Card

Create a two sided, high gloss, quality business card for Brightpath Holdings.

Target Market(s)

People wanting to purchase, scale, and sell businesses.

Industry/Entity Type

Entrepreneurs

Contact Information for Business Card

One line: Dana Corwell, CPA, CMA Another line: Entrepreneur & Investor Another line: Business Ownership Transition Expert Another line: Multi-State Licensed Real Estate Broker Phone 954-BRTPATH (278-7284) Email Dana@Brightpath Holdings.com Website www.Brightpath.com

Requirements
Must have
• Black Card, logo on one side, all other information on the other side including a small logo.
Nice to have
• Possibly add a tagline "Helping entrepreneurs live a life they don't need a vacation from"
Should not have
• There will not be a mailing address on these cards.

```html
<!DOCTYPE html>
<html lang="en">
<head>
<meta charset="utf-8">
<title>Brightpath Holdings Business Card</title>
<link rel="stylesheet" href="https://fonts.googleapis.com/css2?family=Montserrat:wght@400;500;800&display=swap">
<style>
  :root {
    --bg: #d9d9d9;
    --card-dark: #1f1d1e;
    --card-mid: #3a393a;
    --gold: #e8aa16;
    --gold-light: #f0bd3c;
    --gold-text: #d9b04a;
    --text-light: #f2f2f2;
    --text-dark: #2a2a2a;
  }
  * { box-sizing: border-box; margin: 0; padding: 0; }
  html, body { width: 1200px; height: 1200px; overflow: hidden; }
  body {
    background: var(--bg);
    font-family: "Montserrat", sans-serif;
    display: flex;
    flex-direction: column;
    align-items: center;
    justify-content: center;
    gap: 60px;
  }
  .card {
    position: relative;
    width: 840px;
    height: 480px;
    border-radius: 28px;
    overflow: hidden;
    background: linear-gradient(135deg, var(--card-mid) 0%, var(--card-dark) 55%);
  }
  .card-back .pattern {
    position: absolute;
    inset: 0;
    background: linear-gradient(135deg, #4a494a 0%, #2b2a2b 50%, #1f1d1e 100%);
  }
  .brand {
    font-weight: 800;
    color: var(--gold-text);
    letter-spacing: 0.5px;
    display: flex;
    align-items: center;
    gap: 12px;
    white-space: nowrap;
  }
  .brand-dot {
    width: 14px; height: 14px; border-radius: 50%;
    background: var(--gold-text);
    flex: none;
  }
  .card-back .brand {
    position: absolute;
    right: 100px;
    bottom: 120px;
    font-size: 32px;
  }
  .card-front .brand {
    position: absolute;
    left: 60px;
    top: 176px;
    width: 360px;
    font-size: 30px;
  }
  .person {
    position: absolute;
    left: 445px;
    top: 52px;
  }
  .person-name {
    font-weight: 800;
    font-size: 34px;
    color: var(--gold);
  }
  .person-role {
    font-weight: 500;
    font-size: 20px;
    color: var(--text-light);
    margin: 6px 0 0 18px;
  }
  .contact {
    list-style: none;
    position: absolute;
    left: 462px;
    top: 150px;
    color: var(--text-light);
    font-size: 19px;
    font-weight: 500;
  }
  .contact li {
    display: flex;
    align-items: center;
    gap: 12px;
    margin-bottom: 8px;
    white-space: nowrap;
  }
  .contact svg { width: 18px; height: 18px; flex: none; }
  .credentials {
    position: absolute;
    left: 70px;
    bottom: 90px;
    right: 40px;
    color: var(--text-light);
    font-size: 19px;
    font-weight: 500;
    line-height: 1.55;
  }
  .credentials .sep { color: var(--gold); padding: 0 4px; }
  .tagline-band {
    position: absolute;
    left: 0; right: 0; bottom: 0;
    height: 62px;
    background: linear-gradient(90deg, var(--gold-light), var(--gold));
    display: flex;
    align-items: center;
    justify-content: center;
    color: var(--text-dark);
    font-size: 20px;
    font-weight: 500;
  }
</style>
</head>
<body>
  <section class="card card-back">
    <div class="pattern" role="img" aria-label="Repeating pattern of faint compass rose motifs on a dark background"></div>
    <div class="brand"><span class="brand-dot"></span>Brightpath Holdings</div>
  </section>

  <section class="card card-front">
    <div class="brand">Brightpath Holdings</div>

    <div class="person">
      <h1 class="person-name">Dana Hale</h1>
      <p class="person-role">Founder &amp; Director</p>
    </div>

    <ul class="contact">
      <li>
        <svg viewBox="0 0 24 24" aria-hidden="true"><path fill="#e8aa16" d="M6.6 10.8a15 15 0 0 0 6.6 6.6l2.2-2.2c.3-.3.7-.4 1-.2 1.1.4 2.3.6 3.6.6.6 0 1 .4 1 1V20c0 .6-.4 1-1 1A17 17 0 0 1 3 4c0-.6.4-1 1-1h3.5c.6 0 1 .4 1 1 0 1.3.2 2.5.6 3.6.1.3 0 .7-.2 1z"/></svg>
        954-BRTPATH (278-7284)
      </li>
      <li>
        <svg viewBox="0 0 24 24" aria-hidden="true"><rect x="2" y="5" width="20" height="14" rx="2" fill="#e8aa16"/><path d="M3 6l9 7 9-7" fill="none" stroke="#1f1d1e" stroke-width="1.8"/></svg>
        Dana@BrightpathHoldings.com
      </li>
      <li>
        <svg viewBox="0 0 24 24" aria-hidden="true"><circle cx="12" cy="12" r="9" fill="none" stroke="#e8aa16" stroke-width="2"/><path d="M3 12h18M12 3c3 3 3 15 0 18M12 3c-3 3-3 15 0 18" fill="none" stroke="#e8aa16" stroke-width="1.6"/></svg>
        www.Brightpath.com
      </li>
    </ul>

    <div class="credentials">
      <p>Dana Corwell, CPA, CMA<span class="sep">|</span>Business Ownership Transition Expert<span class="sep">|</span></p>
      <p>Entrepreneur &amp; Investor<span class="sep">|</span>Multi-State Licensed Real Estate Broker</p>
    </div>

    <div class="tagline-band">Helping entrepreneurs live a life they don’t need a vacation from</div>
  </section>
</body>
</html>
```